High End Business Card Design for Flooring Store

Looking for a new card design for our hardwood flooring company. We have no print budget for these and are open to cards made from wood, metal, cardstock with embossed print ... or any combination of these. No plastic.

We sell luxury products and I want the cards to reflect our image of quality and class.

Our contact information as such;
Employee Name
418 Colbrook Blvd.
Ostrel, KR
K9R-3M5
(555) 214-3968
Employee email @velkaflooring.com

Target Market(s)

Home Builders

Contact Information for Business Card

Emnployee name, business contact information

```html
<!DOCTYPE html>
<html lang="en">
<head>
<meta charset="utf-8">
<title>Velka Flooring – Business Card</title>
<link rel="stylesheet" href="https://fonts.googleapis.com/css2?family=Montserrat:wght@400;500&family=Ubuntu:wght@400&display=swap">
<style>
  :root {
    --backdrop: #cccccc;
    --paper: #ffffff;
    --brand-red: #922a26;
    --brand-gold: #e8b427;
    --ink: #1c1c1c;
    --slate: #5f5f5f;
    --card-shadow: 4px 6px 10px rgba(0,0,0,0.25);
  }
  * { margin: 0; padding: 0; box-sizing: border-box; }
  html, body {
    width: 1200px; height: 1200px; overflow: hidden;
    background: var(--backdrop);
  }
  .canvas { position: relative; width: 1200px; height: 1200px; }

  .card {
    position: absolute; left: 169px; width: 865px; height: 505px;
    box-shadow: var(--card-shadow); overflow: hidden;
  }
  .card--front { top: 75px; background: var(--paper); }
  .card--back { top: 619px; background: var(--brand-gold); }

  .card__bands { position: absolute; inset: 0; width: 100%; height: 100%; }

  .brand {
    position: absolute; display: flex; flex-direction: column; align-items: center;
    font-family: 'Montserrat', sans-serif;
  }
  .brand__row { display: flex; align-items: center; }
  .brand__name { color: var(--brand-red); font-weight: 400; line-height: 1; }
  .brand__tag { color: var(--slate); font-weight: 500; line-height: 1.2; text-align: center; }

  .card--front .brand { left: 490px; top: 92px; width: 360px; }
  .card--front .brand__mark { width: 34px; height: 34px; background: var(--brand-gold); margin-right: 12px; }
  .card--front .brand__name { font-size: 78px; }
  .card--front .brand__tag { font-size: 18.5px; margin-top: 0; }

  .card--back .brand { left: 0; width: 100%; top: 168px; }
  .card--back .brand__mark { width: 60px; height: 60px; background: var(--slate); margin-right: 18px; }
  .card--back .brand__name { font-size: 128px; }
  .card--back .brand__tag { font-size: 30px; margin-top: 0; }

  .employee-name {
    position: absolute; left: 71px; top: 234px;
    font-family: 'Ubuntu', sans-serif; font-size: 35px; color: var(--paper); line-height: 1;
  }

  .contact {
    position: absolute; font-family: 'Ubuntu', sans-serif; font-size: 21px; line-height: 34px;
  }
  .contact--direct { left: 71px; top: 375px; color: var(--ink); }
  .contact--address { right: 58px; top: 342px; color: var(--paper); text-align: right; }
  .contact__line { display: flex; align-items: center; gap: 10px; white-space: nowrap; }
  .contact--address .contact__line { justify-content: flex-end; }
  .contact__icon { width: 18px; height: 18px; flex: none; }
  .contact__spacer { width: 18px; flex: none; }
</style>
</head>
<body>
<main class="canvas">

  <section class="card card--front" aria-label="Business card front">
    <svg class="card__bands" viewBox="0 0 692 404" preserveAspectRatio="none" aria-hidden="true">
      <polygon fill="var(--brand-red)" points="0,160 332,160 398,220 692,220 692,404 474,404 304,250 0,250"/>
      <polygon fill="var(--brand-gold)" points="0,250 304,250 474,404 0,404"/>
    </svg>

    <div class="brand">
      <div class="brand__row">
        <span class="brand__mark"></span>
        <span class="brand__name">Velka</span>
      </div>
      <p class="brand__tag">Planchers &amp; Escaliers<br>Flooring &amp; Stairs</p>
    </div>

    <p class="employee-name">Employee Name</p>

    <div class="contact contact--direct">
      <p class="contact__line">
        <svg class="contact__icon" viewBox="0 0 18 18" aria-hidden="true"><rect x="5" y="1.5" width="8" height="15" rx="1.5" fill="none" stroke="var(--ink)" stroke-width="1.8"/><rect x="7.5" y="13" width="3" height="1.4" fill="var(--ink)"/></svg>
        (555) 214-3968
      </p>
      <p class="contact__line">
        <svg class="contact__icon" viewBox="0 0 18 18" aria-hidden="true"><rect x="2" y="4" width="14" height="10" rx="1" fill="var(--ink)"/><polyline points="2.5,4.8 9,9.5 15.5,4.8" fill="none" stroke="var(--paper)" stroke-width="1.3"/></svg>
        email @velkaflooring.com
      </p>
    </div>

    <div class="contact contact--address">
      <p class="contact__line">
        418 Colbrook Blvd.
        <svg class="contact__icon" viewBox="0 0 18 18" aria-hidden="true"><path d="M9 1.5a5.5 5.5 0 0 0-5.5 5.5c0 4 5.5 9.5 5.5 9.5s5.5-5.5 5.5-9.5A5.5 5.5 0 0 0 9 1.5z" fill="var(--paper)"/><circle cx="9" cy="7" r="2" fill="var(--brand-red)"/></svg>
      </p>
      <p class="contact__line">Ostrel, KR<span class="contact__spacer"></span></p>
      <p class="contact__line">K9R-3M5<span class="contact__spacer"></span></p>
    </div>
  </section>

  <section class="card card--back" aria-label="Business card back">
    <div class="brand">
      <div class="brand__row">
        <span class="brand__mark"></span>
        <span class="brand__name">Velka</span>
      </div>
      <p class="brand__tag">Planchers &amp; Escaliers<br>Flooring &amp; Stairs</p>
    </div>
  </section>

</main>
</body>
</html>
```